transgender support group needs innovative business card and logo

we are a transgender support group looking for a new logo and business card. I would like to include a Mona Lisa head (our logo), over top of, or somehow incorporate a rainbow (an LGBT symbol) arcing over the lower left third of the card, allowing for the text on the remaining part. Other designs are welcome, as this is just some guidance to start. I would like "MERIDAN" to possibly be larger the the "education association", and under that, I would like "a transgender resource" We also need room for the address, website and phone number. A bit larger, would need to be a spot for a name and title.
Meridian Learning Association, 412 Pine Hollow mill rd. Hollisford qx18532 suite 346. phone 555 010 0147 contact person Marlene Osterby, president

```html
<!DOCTYPE html>
<html lang="en">
<head>
<meta charset="utf-8">
<title>Meridian Learning Association – Business Card</title>
<link rel="stylesheet" href="https://fonts.googleapis.com/css2?family=Gelasio:wght@500;700&family=Roboto:wght@400&display=swap">
<style>
  :root {
    --page-bg: #e4e1dc;
    --card-light: #f6f6f5;
    --card-mid: #dcdfe2;
    --navy-deep: #172a4f;
    --navy-light: #32507e;
    --ink-dark: #262626;
    --name-tone: #b7ad9e;
    --contact-tone: #d4d0cb;
    --address-tone: #c7bcc2;
    --portrait-warm: #a57a2c;
    --portrait-dark: #3d3a1f;
  }
  * { margin: 0; padding: 0; box-sizing: border-box; }
  html, body {
    width: 1200px;
    height: 970px;
    overflow: hidden;
    background: var(--page-bg);
  }
  .business-card {
    position: absolute;
    left: 65px;
    top: 166px;
    width: 1070px;
    height: 638px;
    overflow: hidden;
    background: linear-gradient(160deg, var(--card-light) 0%, var(--card-mid) 55%, var(--card-light) 100%);
    box-shadow: 0 8px 24px rgba(0,0,0,0.18);
  }
  .wave-band {
    position: absolute;
    inset: 0;
    width: 1070px;
    height: 638px;
  }
  .portrait-area {
    position: absolute;
    left: 310px;
    top: 30px;
    width: 154px;
    height: 230px;
    background: linear-gradient(180deg, var(--portrait-dark) 0%, var(--portrait-warm) 45%, var(--portrait-dark) 100%);
  }
  .org-name {
    position: absolute;
    left: 58px;
    top: 272px;
    font-family: "Gelasio", Georgia, serif;
    font-weight: 700;
    font-size: 45px;
    color: var(--ink-dark);
    white-space: nowrap;
  }
  .org-tagline {
    position: absolute;
    left: 160px;
    top: 332px;
    font-family: "Roboto", Arial, sans-serif;
    font-size: 30px;
    color: var(--ink-dark);
    white-space: nowrap;
  }
  .contact-block {
    position: absolute;
    right: 45px;
    top: 388px;
    text-align: right;
    white-space: nowrap;
  }
  .person-name {
    font-family: "Gelasio", Georgia, serif;
    font-weight: 500;
    font-size: 47px;
    line-height: 58px;
    color: var(--name-tone);
  }
  .person-title {
    font-family: "Roboto", Arial, sans-serif;
    font-size: 30px;
    line-height: 40px;
    color: var(--contact-tone);
  }
  .contact-line {
    position: absolute;
    right: 47px;
    display: flex;
    align-items: center;
    gap: 47px;
    font-family: "Roboto", Arial, sans-serif;
    font-size: 32px;
    white-space: nowrap;
  }
  .contact-line.phone { top: 520px; color: var(--contact-tone); }
  .contact-line.address { top: 568px; color: var(--address-tone); }
  .contact-icon { width: 24px; height: 24px; display: block; }
</style>
</head>
<body>
  <div class="business-card">
    <svg class="wave-band" viewBox="0 0 1070 638" aria-hidden="true">
      <defs>
        <linearGradient id="navyFill" x1="0" y1="0" x2="1" y2="0">
          <stop offset="0" stop-color="var(--navy-light)"/>
          <stop offset="0.5" stop-color="var(--navy-light)"/>
          <stop offset="1" stop-color="var(--navy-deep)"/>
        </linearGradient>
      </defs>
      <path d="M0 402 C 260 432, 700 425, 1070 208 L 1070 638 L 0 638 Z" fill="url(#navyFill)"/>
    </svg>

    <div class="portrait-area" role="img" aria-label="Renaissance-style portrait painting used as the association emblem"></div>

    <h1 class="org-name">Meridian Learning Association</h1>
    <p class="org-tagline">a transgender resource</p>

    <div class="contact-block">
      <p class="person-name">Marlene Osterby</p>
      <p class="person-title">president</p>
    </div>

    <p class="contact-line phone">
      <span>555 010 0147</span>
      <svg class="contact-icon" viewBox="0 0 24 24" aria-label="phone" role="img">
        <rect width="24" height="24" fill="var(--contact-tone)"/>
        <path d="M7 4 L10 4 L11 8 L9 9.5 C10 12.5 11.5 14 14.5 15 L16 13 L20 14 L20 17 C20 19 18 20 16 19.5 C10 18 6 14 4.5 8 C4 6 5 4 7 4 Z" fill="var(--navy-deep)"/>
      </svg>
    </p>

    <p class="contact-line address">
      <span>412 Pine Hollow mill rd.&nbsp; Hollisford qx18532 suite 346.</span>
      <svg class="contact-icon" viewBox="0 0 24 24" aria-label="location" role="img">
        <rect width="24" height="24" fill="var(--address-tone)"/>
        <path d="M12 4 C8.7 4 7 6.4 7 9 C7 12.5 12 19 12 19 C12 19 17 12.5 17 9 C17 6.4 15.3 4 12 4 Z" fill="var(--navy-deep)"/>
        <circle cx="12" cy="9" r="2" fill="var(--address-tone)"/>
      </svg>
    </p>
  </div>
</body>
</html>
```